Upgrade your eyecare

Print advertisement (newspaper, magazine). Add for optometry office and optical boutique "Harlowmere Vision Partners." We provide eye exams and eyewear with cutting edge technology and are located in a tech-savy college town. We would like the add to mimic an orbitel (or kelvo?) screen for app update/upgrades. We want to attract new customers / patients who are tech savy and would appreciate a high-tech medical office. Something like: 'Eyecare and eye wear app' uprade available, with some graphics like swipe to upgrade, etc. See www.harlowmerevision.example for some of our color schemes and graphics

Reason: I apologize if the brief was unclear. I am looking for something to print in newspaper and magazines, size about 6"x6". The idea is that your eyes deserve the best technology, so I wanted to tie into the smartphone generation by using kelvo or orbitel imagery about an upgrade is available. It could be someone holding a phone with some text/logos, it could be more abstract. There are some great ideas, but I feel some people may want/need a few more days to fine tune submissions, so I'm extending it a few days. Thanks everyone! Please ask any questions.

```html
<!DOCTYPE html>
<html lang="en">
<head>
<meta charset="utf-8">
<title>Harlowmere Vision Partners – Upgrade</title>
<link href="https://fonts.googleapis.com/css2?family=Michroma&family=Roboto:wght@300&display=swap" rel="stylesheet">
<style>
  :root {
    --plum: #6e2468;
    --plum-light: #b58fb2;
    --grey-text: #6d6d6d;
    --grey-soft: #9a9a9a;
    --paper: #ffffff;
  }
  html, body {
    margin: 0;
    padding: 0;
    overflow: hidden;
    background: #ffffff;
  }
  .ad {
    position: relative;
    width: 929px;
    height: 1200px;
    background: var(--plum);
    overflow: hidden;
  }
  .ad__sheet {
    position: absolute;
    left: 33px;
    top: 33px;
    width: 863px;
    height: 1134px;
    background: var(--paper);
    overflow: hidden;
  }
  .ad__swoosh {
    position: absolute;
    left: 0;
    top: 0;
    width: 863px;
    height: 1134px;
  }
  .brand__mark {
    position: absolute;
    left: 273px;
    top: 68px;
    width: 270px;
    height: 270px;
    box-sizing: border-box;
    border: 14px solid var(--plum);
    border-radius: 10px;
  }
  .brand__name {
    position: absolute;
    left: 0;
    top: 382px;
    width: 863px;
    margin: 0;
    text-align: center;
    font-family: "Michroma", sans-serif;
    font-weight: 400;
    font-size: 46px;
    line-height: 70px;
    letter-spacing: 1px;
    color: var(--plum);
    text-transform: uppercase;
  }
  .contact-phone {
    position: absolute;
    right: 98px;
    top: 550px;
    margin: 0;
    font-family: "Roboto", sans-serif;
    font-weight: 300;
    font-size: 20px;
    letter-spacing: 2px;
    color: var(--grey-text);
  }
  .upgrade {
    position: absolute;
    left: 128px;
    top: 606px;
    display: flex;
    align-items: center;
  }
  .upgrade__label {
    font-family: "Roboto", sans-serif;
    font-weight: 300;
    font-size: 40px;
    letter-spacing: 1px;
    color: var(--grey-text);
    margin-right: 16px;
  }
  .upgrade__chevrons {
    width: 420px;
    height: 64px;
  }
  .contact-address {
    position: absolute;
    right: 98px;
    top: 722px;
    margin: 0;
    text-align: right;
    font-family: "Roboto", sans-serif;
    font-weight: 300;
    font-style: normal;
    font-size: 19px;
    line-height: 25px;
    letter-spacing: 1.5px;
    color: var(--grey-text);
  }
</style>
</head>
<body>
  <main class="ad">
    <section class="ad__sheet">
      <svg class="ad__swoosh" viewBox="0 0 863 1134" aria-hidden="true">
        <defs>
          <linearGradient id="swoosh-back" x1="0" y1="0" x2="0" y2="1">
            <stop offset="0" stop-color="#f4f4f4"/>
            <stop offset="1" stop-color="#d9d9d9"/>
          </linearGradient>
          <linearGradient id="swoosh-front" x1="0" y1="0" x2="1" y2="1">
            <stop offset="0" stop-color="#ffffff"/>
            <stop offset="0.5" stop-color="#e6e6e6"/>
            <stop offset="1" stop-color="#a9a9a9"/>
          </linearGradient>
          <linearGradient id="swoosh-floor" x1="0" y1="0" x2="0" y2="1">
            <stop offset="0" stop-color="#ececec"/>
            <stop offset="1" stop-color="#b4b4b4"/>
          </linearGradient>
        </defs>
        <path d="M0 710 C 220 770, 560 840, 863 770 L 863 1134 L 0 1134 Z" fill="url(#swoosh-back)"/>
        <path d="M0 760 C 300 820, 560 900, 863 1010 L 863 1134 L 0 1134 Z" fill="url(#swoosh-front)" opacity="0.8"/>
        <path d="M0 900 C 250 900, 560 960, 863 1050 L 863 1134 L 0 1134 Z" fill="url(#swoosh-floor)" opacity="0.7"/>
      </svg>

      <div class="brand__mark" aria-hidden="true"></div>
      <h1 class="brand__name">Harlowmere Vision<br>Partners</h1>

      <p class="contact-phone">Phone: (555)014-2020</p>

      <div class="upgrade">
        <span class="upgrade__label">UPGRADE</span>
        <svg class="upgrade__chevrons" viewBox="0 0 420 64" aria-hidden="true">
          <g fill="none" stroke="var(--plum-light)" stroke-width="1.5">
            <path d="M2 2 L32 32 L2 62"/>
            <path d="M62 2 L92 32 L62 62"/>
            <path d="M122 2 L152 32 L122 62"/>
            <path d="M182 2 L212 32 L182 62"/>
            <path d="M242 2 L272 32 L242 62"/>
            <path d="M302 2 L332 32 L302 62"/>
            <path d="M362 2 L392 32 L362 62"/>
          </g>
        </svg>
      </div>

      <address class="contact-address">
        2180 Larkfield Avenue, Suite 2<br>
        Westbrook Commons<br>
        Harlowmere, VA 24099
      </address>
    </section>
  </main>
</body>
</html>
```